Ridgeline Outfitters Business Cards

Recently had a logo done with Artfolio and now looking for a business card to go along with it.

Target Market(s)

Ridgeline Outfitters is a weapons dealer. My market will be primarily men, hunting, shooting type.

Industry/Entity Type

Business

Contact Information for Business Card

I selected double sided, but this is not required, single or double is going to be fine. I picture the logo on one side, or perhaps just the circle which contains "RO" with the remaining info on the other side.

Font styles to use
Sans Serif

Requirements
Must have
• My name: Milo Brandt
• Title: Owner
• tel: 612-555-0187
• web: www.ridgelineoutfittersmn.example
Nice to have
• I like the concept of a black business card. I would like to keep the colors monotone, black, grey, white or red. Red is acceptable because it is in the logo. I have also seen cards that are matte black with shiny black as well, perhaps for the logo (or circle RO) part of the logo.
• I will upload a couple of the logos for use, and also an example I just found of the black on black. and some others that have a nice contrast.
Should not have
• lots of colors are not wanted.

```html
<!DOCTYPE html>
<html lang="en">
<head>
<meta charset="utf-8">
<title>Ridgeline Outfitters Business Cards</title>
<link rel="stylesheet" href="https://fonts.googleapis.com/css2?family=Open+Sans:wght@400;600&display=swap">
<style>
  :root {
    --page-bg: #9a918d;
    --card-bg: #1b1e27;
    --brand-red: #e3141b;
    --ring-grey: #6e6e70;
    --text-white: #f2f2f2;
    --text-soft: #c9cbd0;
    --rule: #8a8d94;
  }
  * { box-sizing: border-box; margin: 0; padding: 0; }
  html, body { width: 1200px; height: 1200px; overflow: hidden; }
  body {
    background: var(--page-bg);
    font-family: "Open Sans", Arial, sans-serif;
    display: flex;
    flex-direction: column;
    align-items: center;
    justify-content: center;
    gap: 44px;
  }
  .card {
    position: relative;
    width: 900px;
    height: 514px;
    background: var(--card-bg);
    box-shadow: 0 10px 30px rgba(0,0,0,.25);
    overflow: hidden;
  }

  /* Front */
  .front .brand {
    position: absolute;
    left: 140px;
    top: 160px;
    display: flex;
    align-items: center;
    gap: 36px;
  }
  .brand-ring {
    width: 150px; height: 150px;
    border-radius: 50%;
    border: 12px solid var(--ring-grey);
    flex: none;
  }
  .front .brand-name {
    color: var(--brand-red);
    font-weight: 600;
    font-size: 50px;
    letter-spacing: 3px;
    text-transform: uppercase;
    line-height: 1.05;
  }
  .front .web-line {
    position: absolute;
    left: 0; right: 0;
    top: 378px;
    display: flex;
    align-items: center;
    justify-content: center;
    gap: 18px;
    color: var(--text-white);
    font-size: 24px;
    letter-spacing: 1.5px;
  }
  .dots { display: flex; align-items: center; gap: 10px; }
  .dot { border-radius: 50%; background: var(--text-white); }
  .dot.sm { width: 6px; height: 6px; opacity: .6; }
  .dot.md { width: 10px; height: 10px; opacity: .85; }
  .dot.lg { width: 15px; height: 15px; }

  /* Back */
  .back .mark {
    position: absolute;
    left: 80px; top: 110px;
    width: 300px;
    display: flex;
    flex-direction: column;
    align-items: center;
    gap: 22px;
  }
  .back .brand-ring { width: 200px; height: 200px; border-width: 14px; }
  .back .brand-name {
    color: var(--brand-red);
    font-weight: 600;
    font-size: 26px;
    letter-spacing: 2px;
    text-transform: uppercase;
    text-align: center;
  }
  .back .divider {
    position: absolute;
    left: 420px; top: 80px;
    width: 2px; height: 350px;
    background: var(--rule);
  }
  .back .details {
    position: absolute;
    left: 480px; top: 96px;
    width: 380px;
    color: var(--text-white);
  }
  .person-name { font-size: 30px; font-weight: 400; }
  .person-title { font-size: 20px; color: var(--text-soft); margin: 2px 0 0 6px; }
  .rule { height: 2px; background: var(--rule); margin: 18px 0 24px; }
  .contact-list { list-style: none; display: flex; flex-direction: column; gap: 22px; }
  .contact-item { display: flex; align-items: center; gap: 18px; font-size: 21px; }
  .contact-item svg { width: 34px; height: 34px; flex: none; }
  .contact-item.web { font-size: 18px; }
</style>
</head>
<body>

<section class="card front">
  <div class="brand">
    <div class="brand-ring"></div>
    <div class="brand-name">Ridgeline<br>Outfitters</div>
  </div>
  <div class="web-line">
    <span class="dots"><span class="dot sm"></span><span class="dot md"></span><span class="dot lg"></span></span>
    <span>www.ridgelineoutfittersmn.example</span>
    <span class="dots"><span class="dot lg"></span><span class="dot md"></span><span class="dot sm"></span></span>
  </div>
</section>

<section class="card back">
  <div class="mark">
    <div class="brand-ring"></div>
    <div class="brand-name">Ridgeline Outfitters</div>
  </div>
  <div class="divider"></div>
  <div class="details">
    <p class="person-name">Milo Brandt</p>
    <p class="person-title">Owner</p>
    <div class="rule"></div>
    <ul class="contact-list">
      <li class="contact-item">
        <svg viewBox="0 0 34 34" aria-hidden="true"><circle cx="17" cy="17" r="15" fill="none" stroke="#f2f2f2" stroke-width="1.5"/><path d="M12 10c1-1 2-1 3 0l1.5 2.5c.5 1 0 1.8-.7 2.3-.6.4-.6 1 0 2l2 2.3c.8.8 1.4.8 2 .2.6-.7 1.3-1.1 2.3-.6l2.3 1.4c1 .7 1 1.6 0 2.6-2 2-5 1.3-8.5-2.2S10 12 12 10z" fill="#f2f2f2"/></svg>
        <span>612-555-0187</span>
      </li>
      <li class="contact-item">
        <svg viewBox="0 0 34 34" aria-hidden="true"><circle cx="17" cy="17" r="15" fill="none" stroke="#f2f2f2" stroke-width="1.5"/><path d="M9 17l16-7-5 15-3-6z M17 19l8-9" fill="none" stroke="#f2f2f2" stroke-width="1.4" stroke-linejoin="round"/></svg>
        <span>hello@ridgelinemail.example</span>
      </li>
      <li class="contact-item web">
        <svg viewBox="0 0 34 34" aria-hidden="true"><circle cx="17" cy="17" r="15" fill="none" stroke="#f2f2f2" stroke-width="1.5"/><circle cx="17" cy="17" r="8" fill="none" stroke="#f2f2f2" stroke-width="1.3"/><ellipse cx="17" cy="17" rx="3.5" ry="8" fill="none" stroke="#f2f2f2" stroke-width="1.1"/><path d="M9 17h16M10.5 13h13M10.5 21h13" stroke="#f2f2f2" stroke-width="1.1"/></svg>
        <span>www.ridgelineoutfittersmn.example</span>
      </li>
    </ul>
    <div class="rule"></div>
  </div>
</section>

</body>
</html>
```